Truck Wrap for Civil Construction Company

*****UPDATE****
This project is for an executive employee and the design needs to be subtle. I do not want a mobile billboard, I want elegant branding on 10% to 20% of the truck.

We are looking for a truck wrap design to promote our branding. I will upload copies of current logo's and other marketing materials.

I want to see subtle designs for executive use.

The attached logo and business card designs are a good example of the feel that i am looking for.
Updates

Target Market(s)

Construction & land development market

Industry/Entity Type

Construction Company

Requirements
Must have
• Must use same logos, fonts
Nice to have
• LESS IS MORE, Don't feel like every inch of the truck needs something on it.
This truck is used for business and personal use, I don't want a rolling billboard. I want professional branding with a subtle design that uses my current logos and fonts
Should not have
• Do Not just copy my business card and lay it over the truck.

I don't want a blue truck

```html
<!DOCTYPE html>
<html lang="en">
<head>
<meta charset="utf-8">
<title>Kestrel Civil Construction – Truck Wrap</title>
<link rel="stylesheet" href="https://fonts.googleapis.com/css2?family=Montserrat:wght@500&family=Open+Sans:wght@600;700&display=swap">
<style>
  :root {
    --canvas: #ffffff;
    --brand-blue: #2b3c9a;
    --brand-mark-fill: #c9cfe9;
    --band-gray: #9d9ea1;
    --panel-gray-top: #8e9093;
    --panel-gray-bottom: #c9cacc;
    --text-light: #ffffff;
  }
  html, body {
    margin: 0;
    padding: 0;
    width: 1200px;
    height: 864px;
    overflow: hidden;
    background: var(--canvas);
  }
  .wrap-design {
    display: block;
    width: 1200px;
    height: 864px;
  }
  .brand-name {
    font-family: "Montserrat", sans-serif;
    font-weight: 500;
    fill: var(--brand-blue);
  }
  .brand-name-main { font-size: 66px; }
  .brand-name-sub { font-size: 30px; }
  .contact {
    font-family: "Open Sans", sans-serif;
    fill: var(--text-light);
  }
  .contact-web { font-size: 40px; font-weight: 700; }
  .contact-phone { font-size: 46px; font-weight: 700; }
  .contact-email { font-size: 26px; font-weight: 600; }
  .accent-stripe {
    fill: none;
    stroke: var(--brand-blue);
    stroke-width: 8;
    stroke-linecap: round;
    stroke-linejoin: round;
  }
</style>
</head>
<body>
<svg class="wrap-design" viewBox="0 0 1751 1261" xmlns="http://www.w3.org/2000/svg" aria-label="Kestrel Civil Construction truck side wrap graphics">
  <defs>
    <linearGradient id="bed-panel-fill" x1="0" y1="0" x2="0" y2="1">
      <stop offset="0" stop-color="var(--panel-gray-top)"/>
      <stop offset="1" stop-color="var(--panel-gray-bottom)"/>
    </linearGradient>
  </defs>

  <path class="door-band" fill="var(--band-gray)"
        d="M470,850 C476,806 500,790 545,790 L1150,790 L1150,850 Z"/>

  <path class="bed-panel" fill="url(#bed-panel-fill)"
        d="M1165,850 L1300,560 L1664,560 L1584,850 Z"/>

  <path class="accent-stripe" d="M442,835 C452,788 480,770 525,770 L1143,768 L1282,562"/>
  <path class="accent-stripe" d="M1684,562 L1578,840"/>

  <circle class="brand-mark" cx="590" cy="680" r="100" fill="var(--brand-mark-fill)"/>
  <text class="brand-name brand-name-main" x="712" y="706" textLength="396" lengthAdjust="spacing">KESTREL</text>
  <text class="brand-name brand-name-sub" x="713" y="742" textLength="397" lengthAdjust="spacing">CIVIL CONSTRUCTION</text>

  <text class="contact contact-web" x="612" y="832" textLength="451" lengthAdjust="spacingAndGlyphs">www.KestrelCivil.com</text>
  <text class="contact contact-phone" x="1316" y="614" textLength="296" lengthAdjust="spacingAndGlyphs">555.014.2290</text>
  <text class="contact contact-email" x="1310" y="643" textLength="292" lengthAdjust="spacingAndGlyphs">Info@KestrelCivil.com</text>
</svg>
</body>
</html>
```